Need a new logo/business card for a cafe

I need a new logo and business card for a café. The café is called "Ladle", and we have a reputation for making a high quality cup of espresso coffee. I would like the business card design to reflect this "high quality". Our baristas craft our customers coffee with care to achieve this result. I would like to see designs that include a warm latte brown color. The card will be single sided to allow the rear to be used as a loyalty card which means the design will need to include space for our business address, phone number, and facebook page details. The uploaded logo is already in use on the café front window, and if it can be incorporated or used that would be great, but I am open to completely new designs as well. Thank you.
Updates
Thank you to all for the submissions. There's quite a few I like now, the hardest part will be choosing! I've set up a poll for added feedback from my own contacts and will wait on results from that.
Hello, more great designs coming in, thank you very much. There's quite a few that I really like, so my biggest challenge is going to be choosing one. Thanks again for your time, and I'll get onto the hard task of making that choice. Marcia
Industry/Entity Type
Cafe
Look and feel
Each slider illustrates characteristics of the customer's brand and the style your logo design should communicate.

```html
<!DOCTYPE html>
<html lang="en">
<head>
<meta charset="utf-8">
<title>Ladle — Business Card</title>
<link rel="stylesheet" href="https://fonts.googleapis.com/css2?family=Gabriela&display=swap">
<style>
  :root {
    --card-bg: #040302;
    --brand-brown: #6a3119;
    --label-brown: #8d4b2b;
    --value-tan: #b8907a;
  }
  * { margin: 0; padding: 0; box-sizing: border-box; }
  html, body {
    width: 1200px;
    height: 720px;
    overflow: hidden;
    background: var(--card-bg);
  }
  .card {
    position: relative;
    width: 1200px;
    height: 720px;
    background: var(--card-bg);
    font-family: "Gabriela", serif;
  }
  .brand {
    position: absolute;
    left: 590px;
    top: 120px;
    display: flex;
    align-items: center;
    gap: 28px;
    white-space: nowrap;
  }
  .brand-name {
    font-family: "Gabriela", serif;
    font-weight: 400;
    font-size: 120px;
    line-height: 1;
    color: var(--brand-brown);
  }
  .brand-mark {
    flex: 0 0 auto;
    width: 84px;
    height: 84px;
    border-radius: 50%;
    background: var(--brand-brown);
    margin-top: 30px;
  }
  .contact-list {
    position: absolute;
    left: 102px;
    top: 398px;
    list-style: none;
  }
  .contact-row {
    display: flex;
    align-items: baseline;
    height: 80px;
    font-size: 31px;
    line-height: 46px;
    white-space: nowrap;
  }
  .contact-label {
    flex: 0 0 259px;
    width: 259px;
    color: var(--label-brown);
  }
  .contact-value {
    flex: 0 0 auto;
    color: var(--value-tan);
  }
</style>
</head>
<body>
  <main class="card">
    <div class="brand">
      <span class="brand-name">Ladle</span>
      <span class="brand-mark" aria-hidden="true"></span>
    </div>
    <ul class="contact-list">
      <li class="contact-row">
        <span class="contact-label">Address</span>
        <span class="contact-value">: Your Company Address</span>
      </li>
      <li class="contact-row">
        <span class="contact-label">Contact Number</span>
        <span class="contact-value">: Your Contact Details</span>
      </li>
      <li class="contact-row">
        <span class="contact-label">Page Details</span>
        <span class="contact-value">: Your Page Details</span>
      </li>
    </ul>
  </main>
</body>
</html>
```